Label for a new brand of Straight Bourbon

The brand name for this Straight Bourbon is Tollivar Ridge, the origin for the look and feel derives from the history of Elias Marrow marking this trail for settlers going west and became one of the first English speaking settlements, you can find more about it here https://www.pastvaultarchive.com/topics/frontier-trails/hollowpine-path
that region is very famous for the production of Bourbon.
The proof will be 90, alc. by vol. 45% Vol 750 ML.

```html
<!DOCTYPE html>
<html lang="en">
<head>
<meta charset="utf-8">
<title>Tollivar Ridge Straight Bourbon Whiskey Label</title>
<link href="https://fonts.googleapis.com/css2?family=Rye&family=Montserrat:wght@500;600&family=Old+Standard+TT:wght@700&display=swap" rel="stylesheet">
<style>
  :root {
    --page: #f4f4f2;
    --label-green: #11261c;
    --gold: #c9ad82;
    --gold-light: #dcc5a0;
    --gold-dark: #a98c62;
  }
  html, body {
    margin: 0;
    padding: 0;
    width: 1200px;
    height: 1200px;
    overflow: hidden;
    background: var(--page);
  }
  .label {
    position: absolute;
    left: 102px;
    top: 60px;
    width: 996px;
    height: 1080px;
    background: var(--label-green);
    color: var(--gold);
    overflow: hidden;
  }
  .label-lines {
    position: absolute;
    left: 0;
    top: 0;
  }
  .portrait {
    position: absolute;
    left: 377px;
    top: 68px;
    width: 242px;
    height: 242px;
    border-radius: 50%;
    background: radial-gradient(circle at 45% 40%, var(--gold-light), var(--gold) 60%, var(--gold-dark));
  }
  .brand-name {
    margin: 0;
    font-family: "Rye", serif;
    font-weight: 400;
    color: var(--gold-light);
    line-height: 1;
    font-size: 116px;
    letter-spacing: 1px;
  }
  .brand-line {
    position: absolute;
    left: 0;
    width: 100%;
    text-align: center;
    white-space: nowrap;
  }
  .brand-line-one { top: 364px; }
  .brand-line-two { top: 496px; }
  .stat {
    position: absolute;
    width: 320px;
    text-align: center;
    font-family: "Montserrat", sans-serif;
    color: var(--gold);
    line-height: 1;
  }
  .stat-value {
    display: block;
    font-size: 98px;
    font-weight: 600;
  }
  .stat-unit {
    display: block;
    margin-top: 2px;
    font-size: 54px;
    font-weight: 500;
  }
  .stat-proof { left: 170px; top: 706px; }
  .stat-abv { left: 510px; top: 706px; }
  .spirit-type {
    position: absolute;
    left: 204px;
    top: 886px;
    width: 588px;
    height: 86px;
    background: var(--gold);
    color: var(--label-green);
    display: flex;
    align-items: center;
    justify-content: center;
    text-align: center;
    white-space: nowrap;
    font-family: "Old Standard TT", serif;
    font-weight: 700;
    font-size: 31px;
    letter-spacing: 0.5px;
  }
</style>
</head>
<body>
  <main class="label">
    <svg class="label-lines" width="996" height="1080" viewBox="0 0 996 1080" aria-hidden="true">
      <g fill="none" stroke="var(--gold)">
        <polyline points="498,235 199,235 267,352" stroke-width="9"/>
        <polyline points="498,235 797,235 729,352" stroke-width="9"/>
        <polyline points="498,258 246,258 300,352" stroke-width="3"/>
        <polyline points="498,258 750,258 696,352" stroke-width="3"/>
        <g stroke-width="2" stroke-dasharray="8 8">
          <line x1="196" y1="230" x2="126" y2="110"/>
          <line x1="800" y1="230" x2="870" y2="110"/>
          <line x1="424" y1="650" x2="386" y2="704"/>
          <line x1="572" y1="650" x2="610" y2="704"/>
          <line x1="204" y1="994" x2="792" y2="994"/>
        </g>
      </g>
      <g fill="var(--gold)">
        <polygon points="436,652 560,652 498,758"/>
        <polygon points="262,572 286,555 286,589"/>
        <polygon points="734,572 710,555 710,589"/>
      </g>
    </svg>

    <div class="portrait" role="img" aria-label="Engraved profile portrait of the frontier trailblazer in a gold circular medallion"></div>

    <h1 class="brand-name">
      <span class="brand-line brand-line-one">TOLLIVAR</span>
      <span class="brand-line brand-line-two">RIDGE</span>
    </h1>

    <div class="stat stat-proof">
      <span class="stat-value">90</span>
      <span class="stat-unit">PROOF</span>
    </div>
    <div class="stat stat-abv">
      <span class="stat-value">45%</span>
      <span class="stat-unit">ALC/VOL</span>
    </div>

    <div class="spirit-type">STRAIGHT BOURBON WHISKEY</div>
  </main>
</body>
</html>
```